Breakthrough Sports Drink Needs a Label Design

Using the logo provided, we need a label design for a new sports drink company called 'Vorna'. We have developed a clear and light, protein-infused beverage for elite athletes.

We would like to label to use a similar color scheme as the logo provided. It needs to portray a refreshing, healthy feel but also needs to reflect the functional aspects of the drink.

The label needs to clearly include the phrases: "18 grams of protein", "For the Elite Athlete" and " "2:1 ratio of carbs to protein "

Target Market(s)

College Athletes

Industry/Entity Type

It Company

Requirements
Must have
• Should be based on the logo provided and include the phrases:
• 18g of Protein
• For The Elite Athlete
• 2:1 Ratio of Carbs to Protein

```html
<!DOCTYPE html>
<html lang="en">
<head>
<meta charset="utf-8">
<title>Vorna Athletic Recovery Label</title>
<link href="https://fonts.googleapis.com/css2?family=Montserrat:wght@300;500;600&family=Roboto+Condensed:wght@400&display=swap" rel="stylesheet">
<style>
  :root {
    --deep-navy: #07141f;
    --panel-dark: #0b2030;
    --sky-blue: #2f8fd6;
    --indigo: #3a3a9e;
    --violet: #4b2a7a;
    --plum: #2c1a45;
    --silver: #dfe4ea;
    --ice-white: #f4f7fa;
    --recovery-blue: #8cbcf0;
    --protein-blue: #5ec6f2;
    --ratio-green: #8dc63f;
  }
  * { margin: 0; padding: 0; box-sizing: border-box; }
  html, body { width: 1200px; height: 727px; overflow: hidden; background: var(--deep-navy); }
  .label {
    position: relative;
    width: 1200px;
    height: 727px;
    overflow: hidden;
    font-family: "Montserrat", sans-serif;
    color: var(--ice-white);
  }
  .label__backdrop {
    position: absolute;
    inset: 0;
    background:
      radial-gradient(ellipse at 30% 35%, rgba(47,143,214,0.85), transparent 60%),
      radial-gradient(ellipse at 80% 30%, rgba(47,143,214,0.55), transparent 55%),
      linear-gradient(160deg, var(--indigo) 0%, var(--sky-blue) 35%, var(--indigo) 65%, var(--plum) 100%);
  }
  .label__shapes { position: absolute; inset: 0; width: 100%; height: 100%; }
  .tagline {
    position: absolute;
    left: 0; right: 0;
    text-align: center;
    font-weight: 300;
  }
  .tagline--small { top: 33px; font-size: 16px; letter-spacing: 1.5px; font-weight: 500; }
  .tagline--large { top: 52px; font-size: 35px; letter-spacing: 2px; }
  .brand-name {
    position: absolute;
    left: 600px;
    top: 342px;
    transform: translate(-50%, -50%) rotate(-90deg);
    font-size: 118px;
    font-weight: 500;
    letter-spacing: 14px;
    color: var(--silver);
    white-space: nowrap;
    line-height: 1;
  }
  .product-line {
    position: absolute;
    top: 608px;
    left: 0; right: 0;
    text-align: center;
    font-size: 23px;
    font-weight: 600;
    letter-spacing: 20px;
    padding-left: 20px;
    color: var(--recovery-blue);
  }
  .claim {
    position: absolute;
    left: 0; right: 0;
    text-align: center;
    font-family: "Roboto Condensed", sans-serif;
    font-size: 27px;
  }
  .claim--protein { top: 646px; color: var(--protein-blue); }
  .claim--ratio { top: 677px; color: var(--ratio-green); }
</style>
</head>
<body>
<main class="label">
  <div class="label__backdrop" role="img" aria-label="Blue and violet faceted background with a faint network of glowing dots and connecting lines"></div>
  <svg class="label__shapes" viewBox="0 0 1500 909" preserveAspectRatio="none" aria-hidden="true">
    <defs>
      <linearGradient id="panelShade" x1="0" y1="0" x2="0" y2="1">
        <stop offset="0" stop-color="#050d15"/>
        <stop offset="0.6" stop-color="#0b2030"/>
        <stop offset="1" stop-color="#0f2a40"/>
      </linearGradient>
    </defs>
    <path class="glow-bowl" d="M378,460 C378,250 470,180 560,250 L940,250 C1030,180 1122,250 1122,460 C1122,710 950,860 750,860 C550,860 378,710 378,460 Z" fill="#ffffff" fill-opacity="0.16"/>
    <path class="center-panel" d="M185,0 H1315 V82 H1300 C1100,82 1000,190 985,320 C965,520 900,780 750,805 C600,780 535,520 515,320 C500,190 400,82 200,82 H185 Z" fill="url(#panelShade)"/>
  </svg>

  <p class="tagline tagline--small">FOR THE</p>
  <h2 class="tagline tagline--large">ELITE ATHLETE</h2>
  <h1 class="brand-name">VORNA</h1>
  <p class="product-line">ATHLETIC RECOVERY</p>
  <p class="claim claim--protein">18g of Protein</p>
  <p class="claim claim--ratio">2:1 Ratio of Carbs to Protein</p>
</main>
</body>
</html>
```